Land Buying Company Needs Letterhead for Direct Mail Marketing to Land Owners

We are looking for a professional letterhead that we will be including in our direct mail marketing. We will be sending this to land owners who may be interested in selling or purchasing land.

The letterhead needs to be editable. Headers and footers would look nice, but we are open. We would want it to include our address, website, phone, and email info. For right now the address to use for design purposes would the following:

Address: 415 Bramwell Avenue #600
Dallas, TX 75219
Website - www.quillridgeacres.example
Email - info@quillridgeacres.example
Phone - 866-402-ACRE

I have attached our logo zip file that we just had done on Pixel Guild. Let me know what questions you have, and thank you.

```html
<!DOCTYPE html>
<html lang="en">
<head>
<meta charset="utf-8">
<title>Quill Ridge Acres — Letterhead</title>
<link rel="stylesheet" href="https://fonts.googleapis.com/css2?family=Montserrat:wght@700&family=Source+Sans+3:wght@400&display=swap">
<style>
  :root {
    --forest: #336600;
    --lime: #8cf01a;
    --sage: #e5eadc;
    --paper: #ffffff;
  }
  html, body {
    margin: 0;
    padding: 0;
    overflow: hidden;
    background: var(--paper);
  }
  .letterhead {
    position: relative;
    width: 855px;
    height: 1200px;
    overflow: hidden;
    background: var(--paper);
    font-family: "Source Sans 3", sans-serif;
    color: var(--forest);
  }
  .brand {
    position: absolute;
    left: 74px;
    top: 77px;
    display: flex;
    align-items: center;
    gap: 12px;
  }
  .brand-dot {
    width: 82px;
    height: 82px;
    border-radius: 50%;
    background: var(--forest);
  }
  .brand-name {
    font-family: "Montserrat", sans-serif;
    font-weight: 700;
    font-size: 27px;
    letter-spacing: 1px;
    color: var(--forest);
    margin: 0;
  }
  .contact {
    position: absolute;
    left: 568px;
    top: 84px;
    margin: 0;
    padding: 0;
    list-style: none;
    font-size: 14px;
    line-height: 25px;
  }
  .contact-label {
    display: inline-block;
    width: 26px;
    color: var(--lime);
  }
  .contact-value {
    color: var(--forest);
  }
  .address {
    position: absolute;
    left: 74px;
    top: 1133px;
    margin: 0;
    font-size: 14px;
    color: var(--forest);
  }
  .corner-arc {
    position: absolute;
    left: 0;
    top: 0;
  }
</style>
</head>
<body>
  <div class="letterhead">
    <svg class="corner-arc" width="855" height="1200" viewBox="0 0 855 1200" aria-hidden="true">
      <circle cx="736" cy="1221" r="301" fill="var(--sage)"/>
    </svg>

    <header class="brand">
      <div class="brand-dot" aria-hidden="true"></div>
      <h1 class="brand-name">QUILL RIDGE ACRES</h1>
    </header>

    <ul class="contact">
      <li><span class="contact-label">T:</span><span class="contact-value">866-402-ACRE</span></li>
      <li><span class="contact-label">E:</span><span class="contact-value">info@quillridgeacres.example</span></li>
      <li><span class="contact-label">W:</span><span class="contact-value">www.quillridgeacres.example</span></li>
    </ul>

    <p class="address">415 Bramwell Avenue #600 Dallas, TX 75219</p>
  </div>
</body>
</html>
```